Real Estate - Property Management Business needs a Landlords Handbook designed

We need a landlord's handbook designed. We are a specialist property management business. The text and logos are there. The book needs images and to present more as a book. We would like to see designs that use orange, grey and white.
Our website is www.tallowbrook.com.au to give you an idea of our brand.

Target Market(s)

Professional couples - property investors

Industry/Entity Type

Real Estate

Font styles to use
Sans Serif

Colors
ffffff
1b1b1b
f37122

Requirements
Must have
• Images of property owners and applicable images
Nice to have
• The Pemberlys owner handbook is a guide to show you what I am looking for
Should not have
• This needs to look professional. No cartoon images

```html
<!DOCTYPE html>
<html lang="en">
<head>
<meta charset="utf-8">
<title>Tallowbrook – Owner Handbook Spreads</title>
<link href="https://fonts.googleapis.com/css2?family=Open+Sans:ital,wght@0,400;0,600;0,700;1,600&display=swap" rel="stylesheet">
<style>
:root{
  --orange:#f37122;
  --ink:#1b1b1b;
  --footer:#3a3a3a;
  --white:#ffffff;
  --stage:#ebebeb;
  --rule:#d9d9d9;
  --band:#e4e4e4;
  --body:#6a6a6a;
}
*{margin:0;padding:0;box-sizing:border-box}
html,body{width:878px;height:1200px;overflow:hidden;background:var(--stage);font-family:"Open Sans",Arial,sans-serif;color:var(--body)}
.spread{position:absolute;left:188px;width:502px;height:352px;box-shadow:0 2px 6px rgba(0,0,0,.25);background:var(--white)}
.spread-1{top:45px}.spread-2{top:424px}.spread-3{top:804px}
.page{position:absolute;top:0;width:251px;height:352px;background:var(--white);overflow:hidden}
.page-left{left:0;border-right:1px solid var(--rule)}
.page-right{left:251px}
.top-rule{position:absolute;top:0;left:0;right:0;height:6px;background:var(--orange)}
.grey-band{position:absolute;top:6px;left:0;width:75px;bottom:19px;background:linear-gradient(180deg,#f3f3f3,var(--band))}
.footer{position:absolute;left:0;right:0;bottom:0;height:19px;background:var(--footer);display:flex;align-items:center;font-size:4.4px;color:var(--white);font-weight:700}
.footer .tag{font-style:italic;font-weight:600;color:var(--orange)}
.footer-left{padding-left:40px}
.footer-right{justify-content:flex-end;padding-right:32px;font-style:italic}
.folio{position:absolute;bottom:0;width:18px;height:28px;background:var(--orange);color:var(--white);font-size:5px;font-weight:700;display:flex;align-items:center;justify-content:center;padding-top:0}
.folio-left{left:15px}.folio-right{right:15px}
.brand{position:absolute;top:0;width:48px;height:41px;background:var(--white);box-shadow:0 1px 3px rgba(0,0,0,.3);display:flex;flex-direction:column;align-items:center;justify-content:center;gap:3px}
.brand-left{left:17px}.brand-right{right:17px;top:4px}
.brand-mark{width:8px;height:8px;background:var(--orange)}
.brand-name{font-size:6.2px;font-weight:700;color:var(--orange)}
.photo{position:absolute}
.photo-cover{left:0;top:6px;width:251px;height:255px;background:linear-gradient(120deg,#7a3d25 0%,#9b5a3c 18%,#e9e6e2 40%,#d8d0c4 62%,#9a9a9a 100%)}
.cover-panel{position:absolute;left:0;top:261px;width:251px;height:72px;background:var(--orange);padding:10px 15px;color:var(--white);font-size:4.1px;line-height:5.8px}
.cover-panel p+p{margin-top:5px}
.cover-panel .hl{color:var(--ink)}
.portrait{position:absolute;width:68px;height:102px;background:linear-gradient(180deg,#e8e8e8 0%,#cfc3b5 45%,#2d2d2d 100%);border:1px solid var(--rule)}
.section-bar{position:absolute;top:19px;height:17px;background:var(--orange);color:var(--white);font-size:7px;font-weight:700;display:flex;align-items:center;text-transform:uppercase}
.section-bar-right{left:15px;right:15px;justify-content:flex-end;padding-right:12px}
.section-bar-left{left:0;width:236px;padding-left:15px}
.running-head{position:absolute;top:23px;right:15px;font-size:7px;color:#9a9a9a;letter-spacing:.2px}
.bio{position:absolute;width:146px}
.bio h3{font-size:5.4px;font-weight:600;color:var(--orange);margin-bottom:6px}
.bio p{font-size:4.1px;line-height:5.8px;margin-bottom:5px}
.services{position:absolute;font-size:4.1px;line-height:5.7px}
.services p{margin-bottom:5px}
.services ul{list-style:none}
.services li.main{padding-left:6px;position:relative}
.services li.main::before{content:"";position:absolute;left:0;top:2px;width:3px;height:3px;background:var(--orange)}
.services ul.sub{padding-left:10px;list-style:disc}
.services ul.sub2{padding-left:10px;list-style:none}
</style>
</head>
<body>

<!-- Spread 1 -->
<section class="spread spread-1">
  <div class="page page-left">
    <div class="photo photo-cover" role="img" aria-label="Photograph of a smiling professional couple standing at the open front door of their home"></div>
    <div class="top-rule"></div>
    <div class="brand brand-left"><span class="brand-mark"></span><span class="brand-name">Tallowbrook</span></div>
    <div class="cover-panel">
      <p>Tallowbrook is a dynamic and energetic specialist Property Management company, <span class="hl">focused on providing the best service, advice and support to you and your investment.</span></p>
      <p>We continually invest in our team's professional development and learning, along with our systems, procedures and technology to ensure that we are able to provide our clients with the highest level of service.</p>
    </div>
    <div class="footer"></div>
  </div>
  <div class="page page-right">
    <div class="top-rule"></div>
    <div class="grey-band"></div>
    <div class="section-bar section-bar-right">Our team and our services</div>
    <div class="portrait" style="left:14px;top:51px" role="img" aria-label="Portrait photograph of the principal licensee"></div>
    <div class="bio" style="left:90px;top:53px">
      <h3>Maren Whitlock – Principal Licensee</h3>
      <p>Maren is the Director of Property Management for Tallowbrook and has over 13 years experience in the property management industry. Committed to learning and extending her knowledge, Maren holds a business degree majoring in marketing, a property services certificate and is a licensed real estate agent.</p>
      <p>Maren holds a reputation for consistently achieving excellent results within the dynamic areas of residential rental properties and portfolio management. It is her professional approach and strong focus on customer service that sets her apart. She builds strong relationships with owners and tenants alike through clear and detailed communication, prompt follow-ups and a highly organised approach.</p>
      <p>She enjoys the many challenges that she faces on a daily basis in her role and thrives on being able to help clients with all aspects of real estate.</p>
    </div>
    <div class="portrait" style="left:14px;top:217px" role="img" aria-label="Portrait photograph of the trust account administrator"></div>
    <div class="bio" style="left:90px;top:219px">
      <h3>Joanna Pell – Trust Account Administrator</h3>
      <p>Qualified and experienced property professional having over 14 years experience in the real estate industry, making trust account management her specialty. Joanna provides an unprecedented level of quality and professionalism. She feels privileged to be trusted with the responsibility of assisting clients to achieve their financial goals. Being an investor herself enables her to serve all clients with a higher level of understanding whilst being extremely attentive to detail. With an in-depth knowledge of all facets of trust accounting, Joanna sets the bar for the best possible outcome, focused on providing premium service in every instance.</p>
    </div>
    <div class="footer footer-right">Owner Handbooks</div>
    <div class="folio folio-right">1</div>
  </div>
</section>

<!-- Spread 2 -->
<section class="spread spread-2">
  <div class="page page-left">
    <div class="top-rule"></div>
    <div class="brand brand-left"><span class="brand-mark"></span><span class="brand-name">Tallowbrook</span></div>
    <div class="portrait" style="left:15px;top:51px" role="img" aria-label="Portrait photograph of a senior property manager"></div>
    <div class="bio" style="left:91px;top:53px">
      <h3>Corinne Dale – Senior Property Manager</h3>
      <p>Corinne is highly organised and professional in her approach to property management. She consistently delivers her clients with the highest possible results and always delivers outstanding customer service.</p>
      <p>Corinne is extremely thorough in her inspections and is quick to respond to any maintenance and repair issues. She thrives on the fast paced and challenging environment that property management provides on a daily basis.</p>
    </div>
    <div class="portrait" style="left:15px;top:183px" role="img" aria-label="Portrait photograph of the leasing manager"></div>
    <div class="bio" style="left:91px;top:185px">
      <h3>Tessa Lund – Leasing Manager</h3>
      <p>Tessa entered the real estate industry 5 years ago and is passionate about property and property management. She is a young professional striving towards achieving the best attainable results in all that she does. Tessa is highly organised and conscientious and as Leasing Manager she understands the importance of careful tenant selection, thorough application processing and clear communication with our clients and tenants alike. In this ever changing industry Tessa prides herself on her determination to stay atop market trends. Her career focus and positive nature are a great asset to our team.</p>
    </div>
    <div class="footer footer-left">Tallowbrook -&nbsp;<span class="tag">We want to manage your property!</span></div>
    <div class="folio folio-left">2</div>
  </div>
  <div class="page page-right">
    <div class="top-rule"></div>
    <div class="running-head">OUR TEAM</div>
    <div class="portrait" style="left:14px;top:51px" role="img" aria-label="Portrait photograph of a senior property manager"></div>
    <div class="bio" style="left:90px;top:53px">
      <h3>Sabine Farrow – Senior Property Manager</h3>
      <p>Sabine is proud to deliver outstanding customer service with informed, honest advice to tenants and landlords alike. She thoroughly enjoys the fast paced and challenging environment that property management provides on a daily basis, combining over 3 years experience within the industry and a degree in finance. Sabine knows asset management is the primary focus of the role and that it is vital a property is well cared for while being tenanted and that owners see solid, long-term returns on their investment. Sabine stays up to date with the local market and keeps an in-depth knowledge of the industry.</p>
    </div>
    <div class="portrait" style="left:14px;top:183px" role="img" aria-label="Portrait photograph of the administration assistant"></div>
    <div class="bio" style="left:90px;top:185px">
      <h3>Mira Joy Santos – Administration Assistant</h3>
      <p>Mira is the company's support assistant. Resourceful and diligent, she performs administrative as well as marketing tasks such as website and social media management, to ensure that the company reaches both its existing and potential clients on a more personal level.</p>
      <p>Having a positive outlook, Mira sees challenges as opportunities for learning and improving herself professionally.</p>
    </div>
    <div class="footer footer-right">Owner Handbooks</div>
    <div class="folio folio-right">3</div>
  </div>
</section>

<!-- Spread 3 -->
<section class="spread spread-3">
  <div class="page page-left">
    <div class="top-rule"></div>
    <div class="section-bar section-bar-left">What do we do for our management services?</div>
    <div class="services" style="left:33px;top:50px;width:200px">
      <p>Our agency manages the tenancy relationship and relevant tenancy matters on your behalf.</p>
      <p>Below are some of the main services we carry out on your behalf as your managing agent:</p>
      <ul>
        <li class="main">Showing your property<ul class="sub"><li>Organising inspections to show the property to prospective tenants.</li></ul></li>
        <li class="main">Advertising your property<ul class="sub"><li>Using resources such as real estate websites and the agency rent list.</li></ul></li>
        <li class="main">Processing tenancy applications<ul class="sub"><li>Verification and assessment of the tenant's ability to pay rent and ability to care for the property including tenancy database checks.</li></ul></li>
        <li class="main">Lodging rental bonds with the tenancy authority on your behalf<ul class="sub"><li>It is a legal requirement that rental bonds paid by a tenant be paid to the tenancy authority within 10 days of monies being received. Bonds can be no more than 4 x the weekly rent if the rent is $700 per week or less.</li></ul></li>
        <li class="main">Completion of the required tenancy documents to commence the tenancy on your behalf<ul class="sub">
          <li>The General Tenancy Agreement<ul class="sub2"><li>This must be given to the tenant prior to monies being taken.</li></ul></li>
          <li>The entry condition report<ul class="sub2"><li>One copy must be provided to the tenant on or before the day they take possession. The tenant has 3 days to sign and return a copy with any additional comments.</li></ul></li>
          <li>The Information Statement<ul class="sub2"><li>A guide to renting booklet provided to the tenant when giving the agreement for signing.</li></ul></li>
          <li>Body corporate by-laws (if applicable)<ul class="sub2"><li>Our agency on your behalf provides the body corporate by-laws to your tenants, as required by law when the agreement is given for signing.</li></ul></li>
        </ul></li>
      </ul>
    </div>
    <div class="footer footer-left">Tallowbrook -&nbsp;<span class="tag">We want to manage your property!</span></div>
    <div class="folio folio-left">4</div>
  </div>
  <div class="page page-right">
    <div class="top-rule"></div>
    <div class="brand brand-right"><span class="brand-mark"></span><span class="brand-name">Tallowbrook</span></div>
    <div class="services" style="left:22px;top:52px;width:200px">
      <ul>
        <li class="main" style="list-style:none"><ul class="sub"><li>Trust account receipt for rent and bond monies paid<ul class="sub2"><li>Lodge the bond with the tenancy authority as required by law. Bond lodgement form completed and lodged.</li></ul></li></ul></li>
        <li class="main">Accounting on your behalf<ul class="sub"><li>Payment of invoices for maintenance and other instructed matters.</li><li>Disbursement of rental trust funds.</li></ul></li>
        <li class="main">Rent arrears<ul class="sub"><li>Daily rent arrears administration and monitoring.</li><li>Issuing of required statutory notices as required and if applicable.</li><li>Communication with the tenant and the lessor as required.</li></ul></li>
        <li class="main">Maintenance negotiation<ul class="sub"><li>Notifying the lessor of maintenance (as per management agreement instructions)</li><li>Communication with the tenant</li><li>Organising a suitable contractor</li><li>Providing a work order to the contractor</li><li>Following up as required</li><li>Payment of invoice</li><li>Accounting to the lessor accordingly.</li></ul></li>
        <li class="main">Tenancy renewals and negotiation<ul class="sub"><li>Contacting the lessor to verify instructions such as to renew the lease or to provide notice to the tenant to vacate</li><li>Making the renewal lease offer to the tenant</li><li>Negotiating rent increases if applicable</li><li>Following up the tenant</li><li>Tenancy paperwork – a new General Tenancy Agreement</li><li>Lodging bond increases if there has been a rent increase upon renewal as required.</li></ul></li>
        <li class="main">Carrying out our general routine inspections during a tenancy<ul class="sub"><li>Issuing the required entry notice allowing the required statutory time frame to enter the property</li><li>Carrying out the inspection following a lawful travel time</li><li>Completing the best practice inspection report and providing it to the lessor</li><li>Following up tenants or the lessor as required and if necessary.</li></ul></li>
        <li class="main">Carrying out the final inspection upon the ending of the tenancy<ul class="sub"><li>Statutory and best practice letter and procedure requirements.</li></ul></li>
      </ul>
    </div>
    <div class="footer footer-right">Owner Handbooks</div>
    <div class="folio folio-right">5</div>
  </div>
</section>

</body>
</html>
```